An our door sign really promoting our clinic and services

We have a new sports medicine clinic called ASHBRAE SPORTS MEDICINE.
We want to make a really nice external sign at our clinic using a photo of our team we really like. I have attached the photo.
We want to simply include our LOGO and also signs with these slogan options. So we want different signs with these different slogans so we can choose what we really like.
This should be a simple and quite design.

The SLOGANS WE WOULD LIKE TO SEE ON THE SIGN (only one slogan per sign in the drafts)

1. Your Journey. Our Expertise
2. Where better health begins
3. Building the best version of you
4. Your health, in expert hands
5. Reaching new heights in your health
6. Your path to peak performance starts here

I have also included different versions of our logo based on the background and how you set the sign up

So summary
1. Image attached
2. Slogan options we would like to see them all
3. Logo attached (various options based on how you set the background up)
4. Size of sign is 2935mm wide x 1885mm high

```html
<!DOCTYPE html>
<html lang="en">
<head>
<meta charset="utf-8">
<title>Ashbrae Sports Medicine – Exterior Sign</title>
<link href="https://fonts.googleapis.com/css2?family=Exo+2:wght@500;700&display=swap" rel="stylesheet">
<style>
  :root {
    --navy: #2d2f50;
    --white: #ffffff;
    --accent: #3fb6e6;
    --photo-light: #d9d6cf;
    --photo-mid: #8d8a86;
    --photo-dark: #2b2f3a;
  }
  * { margin: 0; padding: 0; box-sizing: border-box; }
  html, body {
    width: 1200px;
    height: 814px;
    overflow: hidden;
    background: var(--navy);
  }
  .sign {
    position: relative;
    width: 1200px;
    height: 814px;
    background: var(--navy);
    font-family: "Exo 2", sans-serif;
  }
  .team-photo {
    position: absolute;
    left: 0;
    top: 0;
  }
  .brand {
    position: absolute;
    left: 100px;
    top: 62px;
    display: flex;
    align-items: center;
    gap: 16px;
  }
  .brand-dot {
    width: 22px;
    height: 22px;
    border-radius: 50%;
    background: var(--accent);
  }
  .brand-name {
    color: var(--white);
    font-weight: 700;
    font-size: 34px;
    line-height: 1;
    letter-spacing: 1px;
  }
  .brand-name span {
    display: block;
    font-size: 17px;
    letter-spacing: 5.6px;
    margin-top: 6px;
  }
  .slogan {
    position: absolute;
    left: 52px;
    top: 296px;
    color: var(--white);
    font-weight: 500;
    font-size: 68px;
    line-height: 86px;
    letter-spacing: 1px;
    text-transform: uppercase;
  }
</style>
</head>
<body>
  <main class="sign">
    <svg class="team-photo" width="1200" height="814" viewBox="0 0 1200 814" role="img" aria-label="Team photo: two clinicians reviewing a tablet in the clinic gym">
      <defs>
        <linearGradient id="photoTone" x1="0" y1="0" x2="0.6" y2="1">
          <stop offset="0" stop-color="var(--photo-light)"/>
          <stop offset="0.45" stop-color="var(--photo-mid)"/>
          <stop offset="1" stop-color="var(--photo-dark)"/>
        </linearGradient>
      </defs>
      <path fill="url(#photoTone)" d="M714,0 C650,20 600,60 572,100 C535,150 540,230 600,268 C662,306 708,330 714,400 C720,455 690,482 688,540 C686,612 722,684 775,704 L1200,704 L1200,0 Z"/>
    </svg>

    <div class="brand">
      <div class="brand-dot"></div>
      <div class="brand-name">ASHBRAE<span>SPORTS MEDICINE</span></div>
    </div>

    <h1 class="slogan">Reaching new<br>heights in<br>your health</h1>
  </main>
</body>
</html>
```